Community Harvest Festival Poster

Seeking a poster design to advertise our community’s annual Harvest Festival. We will utilize and display printed posters as well as distribute PDFs via our weekly e-news letters. This years "theme" is, "Copper Lantern/Maple Ridge Fair, Where City and Country Meet." The vibe is a bohemian, beatnik, street scene, meets a old fashioned orchard.

Target Market(s)

NYC School Community- should appeal to an audience that ranges from kids to grandparents. Very family oriented, with wide appeal, and must be eye catching.

Other font styles liked:
• One style should be more of a "Country" font, the other should have more of a clean city vibe.

Colors
acd037
ffc214
f68e4e
eaf2ce

Requirements
Must have
• The following copy:
• Copper Lantern Maple Ridge Fair
• Where City and Country Meet
• Celebrate C&C With Great Food, Music, Entertainment, And Fun!
• Saturday, October 19th 2019
• 12:00-4:00pm
• Tickets will be available for sale at Drop off and Pick up
Nice to have
• I'm not limited, but a couple of ideas that could be cool:
• One incorporated the background of a street, i.e. pavement, which has leaves blowing over it, and perhaps an apple or two rolling onto the page.
• Another has a diagonal breakup of the image, with one side pavement and the other side rustic wood, also with leaves sweeping across.
• I've also attached images of previous festival posters that I have gravitated to for some idea of quality I'm looking for.
Should not have
• Anything inappropriate for children.

```html
<!DOCTYPE html>
<html lang="en">
<head>
<meta charset="utf-8">
<title>Copper Lantern/Maple Ridge Fair – Harvest Festival</title>
<link href="https://fonts.googleapis.com/css2?family=Pacifico&family=Rye&family=Chewy&family=Nunito:wght@700;800&display=swap" rel="stylesheet">
<style>
  :root{
    --sun:#f6c23e;
    --sun-deep:#f2a93b;
    --tangerine:#f68e4e;
    --ribbon:#f7a21b;
    --ribbon-fold:#d97b10;
    --teal:#3cb7b0;
    --teal-dark:#1f8f8c;
    --rose:#ef5a7c;
    --crimson:#e0344f;
    --paper:#fdfcf8;
    --festival-red:#e8262c;
    --city-blue:#1f78c8;
    --white:#ffffff;
  }
  html,body{margin:0;padding:0;overflow:hidden;background:var(--paper);}
  .poster{
    position:relative;width:853px;height:1200px;overflow:hidden;
    background:var(--paper);font-family:"Nunito",sans-serif;
  }
  .backdrop{position:absolute;inset:0;width:853px;height:1200px;}
  .art{position:absolute;border-radius:40px;}
  .art--guitarist{left:20px;top:10px;width:370px;height:330px;
    background:radial-gradient(circle at 45% 45%,#3aa7b5 0%,#e98a5a 55%,rgba(246,194,62,0) 75%);}
  .art--leaves-top{right:0;top:0;width:330px;height:230px;border-radius:0 0 0 160px;
    background:linear-gradient(200deg,#6fcfc4,#3cb7b0 60%,rgba(60,183,176,0));}
  .art--basket{left:40px;top:790px;width:290px;height:250px;
    background:radial-gradient(circle at 50% 40%,#e5752f 0%,#b8733c 50%,rgba(184,115,60,0) 75%);}
  .art--leaves-bottom{left:0;top:880px;width:260px;height:320px;border-radius:0 160px 0 0;
    background:linear-gradient(20deg,#1f8f8c,#3cb7b0 55%,rgba(60,183,176,0));}
  .art--keyboardist{left:470px;top:860px;width:370px;height:310px;
    background:radial-gradient(circle at 55% 50%,#2f9bb0 0%,#f2c04a 45%,rgba(239,90,124,0) 75%);}
  .title{
    position:absolute;left:230px;top:375px;margin:0;
    font-family:"Pacifico",cursive;font-weight:400;font-size:66px;
    color:var(--festival-red);line-height:1;
  }
  .theme-ribbon{position:absolute;left:60px;top:465px;width:740px;height:140px;}
  .theme{
    position:absolute;left:110px;top:488px;width:640px;margin:0;
    font-family:"Rye",serif;font-size:25px;line-height:1.45;
    color:var(--white);text-align:center;transform:rotate(-4deg);
  }
  .tagline{
    position:absolute;left:90px;top:632px;width:680px;margin:0;
    font-family:"Chewy",cursive;font-size:36px;line-height:1.25;
    color:var(--city-blue);text-align:center;letter-spacing:.5px;
  }
  .date{
    position:absolute;left:0;top:760px;width:853px;margin:0;text-align:center;
    font-weight:800;font-size:29px;color:var(--city-blue);
  }
  .time{
    position:absolute;left:0;top:812px;width:853px;margin:0;text-align:center;
    font-weight:700;font-size:27px;color:var(--city-blue);
  }
  .tickets{
    position:absolute;left:0;top:1146px;width:853px;margin:0;text-align:center;
    font-weight:700;font-size:19px;color:var(--white);
  }
</style>
</head>
<body>
<main class="poster">
  <svg class="backdrop" viewBox="0 0 853 1200" aria-hidden="true">
    <polygon points="0,0 590,0 0,500" fill="var(--sun)"/>
    <polygon points="0,0 300,0 0,250" fill="var(--sun-deep)" opacity=".45"/>
    <polygon points="590,0 640,0 0,545 0,500" fill="var(--teal)"/>
    <polygon points="853,560 853,1200 0,1200 0,1090" fill="var(--rose)"/>
    <polygon points="853,780 853,1200 560,1200" fill="var(--crimson)"/>
  </svg>

  <div class="art art--leaves-top" role="img" aria-label="Large teal tropical leaves"></div>
  <div class="art art--guitarist" role="img" aria-label="Illustrated street musician playing an acoustic guitar with music notes"></div>
  <div class="art art--leaves-bottom" role="img" aria-label="Teal and orange tropical leaves"></div>
  <div class="art art--basket" role="img" aria-label="Wooden bushel basket full of orange apples with falling leaves"></div>
  <div class="art art--keyboardist" role="img" aria-label="Illustrated street musician playing a keyboard"></div>

  <h1 class="title">Festival</h1>

  <svg class="theme-ribbon" viewBox="0 0 740 140" aria-hidden="true">
    <polygon points="0,108 40,98 30,132 0,140" fill="var(--ribbon-fold)"/>
    <polygon points="740,30 700,36 712,2 740,0" fill="var(--ribbon-fold)"/>
    <polygon points="20,48 720,0 735,84 30,132" fill="var(--ribbon)"/>
  </svg>
  <p class="theme">Copper Lantern/Maple Ridge Fair,<br>Where City and Country Meet</p>

  <p class="tagline">Celebrate C&amp;C With Great Food,<br>Music, Entertainment, And Fun!</p>
  <p class="date">Saturday, October 19th 2019</p>
  <p class="time">12:00-4:00pm</p>
  <p class="tickets">Tickets will be available for sale at Drop off and Pick up</p>
</main>
</body>
</html>
```